A stationary and business card desgn for a podiatry clinic

i require a stationary design for letter heads, envelopes, buisness cards.

it is for a new podiatry practise within a medical centre, that deals with all lower limb pathology and injury and foot related problems.

the colour scheme for my exisiting logo is orange blue and white. colours provided below.
i would like a white background for the buisness card.

the final design should portray health and wellbeing in a professional manner that still looks modern but sophisticated.

male and female, off all ethinical backgrounds aged between 30-80 years

Medical

• letter head.
need to include all contact details mentioned below.
need to also include ABN 53208741196

i prefer the logo on the top left hand corner and the contact info on the right. the address can be written in a sentence like form as the footer.

Business card
Front:

include logo provided.

clinic details on the front of the card.

Carla Westbrook
B.Pod

P: 8391 4460
F: 8391 4478
M: 0437 612 809
E: carla@velmora.com.au
W: www.velmora.com.au

(may use icons to indicate contact type)

on back

Appointments:

lines to write dates, time etc.
(3-4 of these)
and a small photo of just the foot from the logo in coloured watermark.

Address:
Larkvale Medical Centre
41 Tambrell Street
Corrindale SA 5117
(this location infomation could be in smaller font at the bottom of the buisness card under a line, running in a sentence like fashion) or in the bottom left or right hand corner in a paragraph like you would write it on an envelope

however if you think a different lay out at the back will look better by all means i just need to have room for the appointment even if it is just lines/ space.

i also prefer square cards not rounded corners.

thanks
• plain texts such as times new roman and arial

```html
<!DOCTYPE html>
<html lang="en">
<head>
<meta charset="utf-8">
<title>Velmora Podiatry – Stationery Set</title>
<link href="https://fonts.googleapis.com/css2?family=Source+Sans+3:wght@400;600;700&display=swap" rel="stylesheet">
<style>
  :root {
    --brand-blue: #213d99;
    --brand-orange: #f26522;
    --paper: #ffffff;
    --backdrop: #f0f0f2;
    --ink: #333333;
    --rule: #9aa3d4;
    --window: #e6e6e8;
    --soft-orange: #fde3d3;
    --soft-blue: #dcdcef;
  }
  * { box-sizing: border-box; margin: 0; padding: 0; }
  html, body { width: 1200px; height: 982px; overflow: hidden; background: var(--backdrop); }
  body { position: relative; font-family: "Source Sans 3", Arial, sans-serif; color: var(--ink); }

  .sheet { position: absolute; background: var(--paper); box-shadow: 3px 3px 6px rgba(0,0,0,.35); }

  .wordmark { position: absolute; display: flex; align-items: center; gap: 8px;
    color: var(--brand-blue); font-weight: 700; line-height: .95; }
  .wordmark__dot { border-radius: 50%; background: var(--brand-orange); flex: none; }

  /* Letterhead */
  .letterhead { left: 24px; top: 24px; width: 660px; height: 933px; }
  .letterhead__band-top { position: absolute; left: 0; top: 0; width: 100%; height: 24px; background: var(--brand-blue); }
  .letterhead__band-foot { position: absolute; left: 0; bottom: 0; width: 100%; height: 26px; background: var(--brand-blue);
    color: #fff; font-size: 9.5px; text-align: center; line-height: 26px; }
  .letterhead .wordmark { left: 25px; top: 62px; font-size: 46px; }
  .letterhead .wordmark__dot { width: 20px; height: 20px; }
  .letterhead__holder { position: absolute; left: 427px; top: 79px; text-align: left; }
  .holder-name { font-weight: 700; font-size: 11.5px; color: #222; }
  .holder-title { font-size: 9px; }
  .letterhead__contacts { position: absolute; left: 525px; top: 79px; padding-left: 8px;
    border-left: 1.5px dotted var(--brand-blue); font-size: 8.5px; line-height: 12.2px; }
  .label { color: var(--brand-orange); font-weight: 600; }

  /* Business card front */
  .card { width: 286px; height: 175px; top: 374px; }
  .card-front { left: 483px; }
  .card-front .wordmark { left: 11px; top: 10px; font-size: 25px; }
  .card-front .wordmark__dot { width: 12px; height: 12px; }
  .card-front__holder { position: absolute; left: 172px; top: 70px; width: 104px; }
  .card-front__holder .holder-name { font-size: 11px; }
  .card-front__holder .holder-title { font-size: 8.5px; padding-bottom: 6px; border-bottom: 1.5px dotted var(--brand-blue); }
  .card-front__contacts { list-style: none; margin-top: 5px; font-size: 8px; line-height: 12.3px; }

  /* Business card back */
  .card-back { left: 791px; overflow: hidden; }
  .card-back__title { position: absolute; left: 12px; top: 9px; font-size: 12px; font-weight: 400; color: #222; }
  .appointment-line { position: absolute; left: 12px; width: 154px; border-top: 1px solid var(--rule); }
  .card-back__watermark { position: absolute; left: 86px; top: 0; width: 200px; height: 175px;
    background: radial-gradient(circle at 68% 40%, var(--soft-orange) 0 22%, transparent 45%),
                radial-gradient(circle at 45% 90%, var(--soft-blue) 0 16%, transparent 36%); }
  .card-back__address { position: absolute; left: 12px; top: 129px; font-size: 7.5px; line-height: 12.5px; font-style: normal; }

  /* Envelope */
  .envelope { left: 485px; top: 572px; width: 692px; height: 345px; }
  .envelope .wordmark { left: 23px; top: 24px; font-size: 25px; }
  .envelope .wordmark__dot { width: 12px; height: 12px; }
  .envelope__rule { position: absolute; left: 26px; top: 88px; height: 233px; border-left: 1.5px dotted var(--brand-blue); }
  .envelope__window { position: absolute; left: 57px; top: 157px; width: 282px; height: 124px;
    background: var(--window); border: 1px solid #444; border-radius: 12px; }
  .envelope__return { position: absolute; left: 30px; top: 313px; font-size: 7.5px; }
</style>
</head>
<body>

  <section class="sheet letterhead" aria-label="Letterhead">
    <div class="letterhead__band-top"></div>
    <div class="wordmark"><span>Velmora<br>Podiatry</span><span class="wordmark__dot"></span></div>
    <div class="letterhead__holder">
      <div class="holder-name">Carla Westbrook</div>
      <div class="holder-title">B.Pod</div>
    </div>
    <div class="letterhead__contacts">
      <div><span class="label">p:</span> 8391 4460</div>
      <div><span class="label">f:</span> 8391 4478</div>
      <div><span class="label">m:</span> 0437 612 809</div>
      <div><span class="label">e:</span> carla@velmora.com.au</div>
      <div><span class="label">w:</span> www.velmora.com.au</div>
      <div>&nbsp;&nbsp;&nbsp;ABN 53208741196</div>
    </div>
    <footer class="letterhead__band-foot">Larkvale Medical Centre, 41 Tambrell Street, Corrindale, SA 5117</footer>
  </section>

  <section class="sheet card card-front" aria-label="Business card front">
    <div class="wordmark"><span>Velmora<br>Podiatry</span><span class="wordmark__dot"></span></div>
    <div class="card-front__holder">
      <div class="holder-name">Carla Westbrook</div>
      <div class="holder-title">B.Pod</div>
      <ul class="card-front__contacts">
        <li><span class="label">p:</span> 8391 4460</li>
        <li><span class="label">f:</span> 8391 4478</li>
        <li><span class="label">m:</span> 0437 612 809</li>
        <li><span class="label">e:</span> carla@velmora.com.au</li>
        <li><span class="label">w:</span> www.velmora.com.au</li>
      </ul>
    </div>
  </section>

  <section class="sheet card card-back" aria-label="Business card back">
    <div class="card-back__watermark" role="img" aria-label="Faint brand watermark in soft orange and blue"></div>
    <h2 class="card-back__title">Appointments</h2>
    <div class="appointment-line" style="top:45px"></div>
    <div class="appointment-line" style="top:68px"></div>
    <div class="appointment-line" style="top:90px"></div>
    <div class="appointment-line" style="top:113px"></div>
    <address class="card-back__address">Larkvale Medical Centre<br>41 Tambrell Street<br>Corrindale SA 5117</address>
  </section>

  <section class="sheet envelope" aria-label="Window envelope">
    <div class="wordmark"><span>Velmora<br>Podiatry</span><span class="wordmark__dot"></span></div>
    <div class="envelope__rule"></div>
    <div class="envelope__window"></div>
    <div class="envelope__return">Larkvale Medical Centre, 41 Tambrell Street, Corrindale SA 5117</div>
  </section>

</body>
</html>
```